Lien Post Card - (5.5 x 8.5)

FRONT OF POSTCARD
Is a Property Lien Putting Your Home at Risk?
HOA Liens • Tax Liens • Municipal Charges • Other Property-Related Liens
You may have options to resolve outstanding liens and protect your home.
A Refinance or Home Equity Line of Credit (HELOC) may help you:
✔ Pay off qualifying liens
✔ Consolidate debt into one manageable payment
✔ Access your home's equity
✔ Improve your financial flexibility
✔ Avoid additional penalties, fees, or collection actions
Don't wait until the situation becomes more difficult.
Call today for a confidential review of your options.
Bluegate Lending Partners, Inc.
(800) 647-2915 x 42
www.bluegatelendco.com
NMLS #381640
BACK OF POSTCARD
Your Home Equity Could Be the Solution
If you have received notices regarding:
• Delinquent Property Taxes
• HOA or Condo Association Assessments
• Municipal Utility Liens
• Special Assessments
• Other Property-Related Obligations
You may qualify for financing options designed to help satisfy those obligations and bring your property current.
Our experienced mortgage professionals can review your situation and discuss available programs, including:
• Cash-Out Refinancing
• Home Equity Lines of Credit (HELOCs)
• Home Equity Loans
• Debt Consolidation Solutions
Free Consultation • No Obligation
Contact Marcus Delaney today at (800) 647-2915 x42 or mdelaney@bluegatelendco.com (NMLS #57308)

```html
<!DOCTYPE html>
<html lang="en">
<head>
<meta charset="utf-8">
<title>Lien Postcard – Front and Back</title>
<link rel="stylesheet" href="https://fonts.googleapis.com/css2?family=Source+Sans+3:wght@400;600;700&family=Oswald:wght@500;600&family=Pacifico&display=swap">
<style>
:root{
  --stage:#a9b7bd;
  --navy:#0a1822;
  --navy-2:#13263a;
  --gold:#d9a036;
  --blue:#1b5593;
  --ink:#111;
  --white:#fff;
}
*{box-sizing:border-box;margin:0;padding:0}
html,body{width:1200px;height:1200px;overflow:hidden}
body{background:var(--stage);font-family:"Source Sans 3",sans-serif;position:relative}
.card{position:absolute;top:230px;width:486px;height:740px;overflow:hidden;box-shadow:0 4px 14px rgba(0,0,0,.25)}
.card > *{position:absolute}
.front{left:100px;background:var(--navy)}
.back{left:614px;background:var(--white)}

/* front */
.front .skyline{left:0;top:0;width:486px;height:420px;
  background:linear-gradient(180deg,#4d5867 0%,#8a6a45 30%,#d38a2a 45%,#4a3520 62%,#1b2633 80%,var(--navy) 100%)}
.front .agent-photo{left:355px;top:238px;width:131px;height:282px;
  background:linear-gradient(180deg,rgba(30,30,35,0) 0%,#262b33 25%,#1b1f26 100%)}
.headline{left:31px;top:18px;color:var(--white);font-weight:700;line-height:1.02}
.headline .sm{font-size:30px;display:block}
.headline .lg{font-size:41px;display:block}
.headline .md{font-size:32px;display:block}
.headline .gold{color:var(--gold)}
.lien-pill{left:0;top:231px;width:290px;height:39px;background:var(--gold);border-radius:0 14px 14px 0;
  padding:3px 0 0 31px;color:var(--navy);font-weight:700;font-size:12px;line-height:1.2}
.intro{left:37px;top:283px;color:var(--white);font-weight:600;font-size:12.5px;line-height:1.1;width:280px}
.help-title{left:31px;top:334px;color:var(--gold);font-weight:700;font-size:14.5px;line-height:1.05;width:280px}
.checklist{left:33px;top:375px;list-style:none;color:var(--white);font-weight:600;font-size:12.5px}
.checklist li{display:flex;gap:6px;margin-bottom:9px;line-height:1.1}
.checklist svg{flex:none;margin-top:2px}
.agent-name{left:307px;top:455px;font-family:"Oswald",sans-serif;font-weight:500;font-size:24px;color:var(--gold);letter-spacing:-.3px}
.agent-title{left:307px;top:487px;color:var(--white);font-weight:600;font-size:10.5px;line-height:1.25}
.gold-band{left:0;top:510px}
.divider{left:191px;top:556px;width:1px;height:158px;background:#c9c9c9}
.brand{left:18px;top:590px;width:160px;display:flex;align-items:center;gap:8px;color:var(--gold);font-weight:700;font-size:14px;line-height:1.1}
.brand .dot{flex:none;width:16px;height:16px;border-radius:50%;background:var(--gold)}
.urgent{left:209px;top:552px;color:var(--gold);font-weight:600;font-size:15px;line-height:1.15;text-transform:uppercase}
.call{left:209px;top:600px;color:var(--white);font-weight:600;font-size:14.5px;line-height:1.2}
.contact-line{display:flex;align-items:center;gap:5px;font-weight:700;font-size:19.5px;line-height:1}
.front .c-phone{left:209px;top:645px;color:var(--white)}
.front .c-web{left:209px;top:674px;color:var(--white)}
.front .nmls{left:209px;top:704px;color:var(--white);font-weight:700;font-size:11px}
.ic{flex:none;width:19px;height:19px;border-radius:50%;background:var(--gold);display:flex;align-items:center;justify-content:center}

/* back */
.couple-photo{left:234px;top:0;width:252px;height:180px;
  background:linear-gradient(90deg,rgba(255,255,255,1) 0%,#e9e4dd 22%,#cfc2b2 60%,#e5ddd2 100%)}
.solution-title{left:31px;top:24px;font-family:"Oswald",sans-serif;font-weight:600;color:var(--blue);font-size:38px;line-height:1.12;letter-spacing:-.5px}
.solution-script{left:34px;top:103px;font-family:"Pacifico",cursive;color:var(--gold);font-size:38px;line-height:1.2}
.rule{left:0;top:180px;width:486px;height:2px;background:var(--gold)}
.col-head{font-weight:700;color:var(--ink);font-size:15.5px;line-height:1.15}
.notices{left:23px;top:222px;width:190px}
.programs{left:232px;top:222px;width:240px}
.bullets{list-style:none;margin-top:10px;color:#222;font-size:14px;line-height:1.05}
.bullets li{position:relative;padding-left:12px;margin-bottom:6px}
.bullets li::before{content:"•";position:absolute;left:0;font-size:11px;top:1px}
.programs .bullets{font-size:12.5px;margin-top:10px}
.programs .bullets li{margin-bottom:6.5px}
.programs p{margin-top:12px;font-weight:700;font-size:11.5px;line-height:1.1;color:var(--ink)}
.offer-band{left:0;top:475px;width:486px;height:58px;background:var(--blue);display:flex;align-items:center}
.offer{display:flex;align-items:center;gap:8px;color:var(--gold);font-weight:700;font-size:18px;position:absolute}
.offer .ring{width:39px;height:39px;border-radius:50%;border:1.5px solid var(--white);display:flex;align-items:center;justify-content:center}
.agent-card{left:30px;top:554px;width:105px;height:146px;border-radius:12px;
  background:linear-gradient(180deg,#d4d6d8 0%,#9a9da2 55%,#2a2d33 100%)}
.contact-script{left:160px;top:551px;font-family:"Pacifico",cursive;font-size:19px;color:var(--ink)}
.back .agent-name{left:160px;top:580px;color:var(--blue);font-size:25px}
.back .agent-title{left:160px;top:612px;color:var(--ink);font-size:10.5px;font-weight:700}
.back .c-phone{left:160px;top:628px;color:var(--ink)}
.back .c-web{left:160px;top:657px;color:var(--ink)}
.back .nmls{left:160px;top:688px;color:var(--ink);font-weight:700;font-size:11px}
.foot-gold{left:0;top:715px;width:243px;height:25px;background:var(--gold)}
.foot-blue{left:243px;top:715px;width:243px;height:25px;background:var(--blue)}
</style>
</head>
<body>

<section class="card front">
  <div class="skyline" role="img" aria-label="City skyline at sunset over a river"></div>
  <div class="agent-photo" role="img" aria-label="Portrait of the mortgage professional in a hat and dark jacket"></div>

  <h1 class="headline">
    <span class="sm">Is a</span>
    <span class="lg">Property Lien</span>
    <span class="md">Putting Your</span>
    <span class="lg">Home</span>
    <span class="lg gold">at Risk?</span>
  </h1>

  <div class="lien-pill">• HOA Liens • Tax Liens • Municipal Charges<br>• Other Property-Related Liens</div>

  <p class="intro">You may have options to resolve outstanding liens and protect your home.</p>
  <p class="help-title">A Refinance or Home Equity Line of Credit (HELOC) may help you:</p>

  <ul class="checklist">
    <li><svg width="11" height="11" viewBox="0 0 11 11"><rect x=".5" y=".5" width="10" height="10" fill="none" stroke="#d9a036"/><path d="M2.5 5.5l2 2 4-5" fill="none" stroke="#d9a036" stroke-width="1.4"/></svg>Pay off qualifying liens</li>
    <li><svg width="11" height="11" viewBox="0 0 11 11"><rect x=".5" y=".5" width="10" height="10" fill="none" stroke="#d9a036"/><path d="M2.5 5.5l2 2 4-5" fill="none" stroke="#d9a036" stroke-width="1.4"/></svg>Consolidate debt into one manageable payment</li>
    <li><svg width="11" height="11" viewBox="0 0 11 11"><rect x=".5" y=".5" width="10" height="10" fill="none" stroke="#d9a036"/><path d="M2.5 5.5l2 2 4-5" fill="none" stroke="#d9a036" stroke-width="1.4"/></svg>Access your home's equity</li>
    <li><svg width="11" height="11" viewBox="0 0 11 11"><rect x=".5" y=".5" width="10" height="10" fill="none" stroke="#d9a036"/><path d="M2.5 5.5l2 2 4-5" fill="none" stroke="#d9a036" stroke-width="1.4"/></svg>Improve your financial flexibility</li>
    <li><svg width="11" height="11" viewBox="0 0 11 11"><rect x=".5" y=".5" width="10" height="10" fill="none" stroke="#d9a036"/><path d="M2.5 5.5l2 2 4-5" fill="none" stroke="#d9a036" stroke-width="1.4"/></svg><span>Avoid additional penalties, fees,<br>or collection actions</span></li>
  </ul>

  <div class="agent-name">MARCUS DELANEY</div>
  <div class="agent-title">TRUSTED MORTGAGE<br>PROFESSIONAL</div>

  <svg class="gold-band" width="486" height="50" viewBox="0 0 486 50"><polygon points="0,19 486,6 486,13 0,44" fill="#d9a036"/></svg>

  <div class="divider"></div>

  <div class="brand"><span class="dot"></span><span>Bluegate Lending Partners, Inc.</span></div>

  <p class="urgent">Don't wait until the situation<br>becomes more difficult.</p>
  <p class="call">Call today for a confidential<br>review of your options.</p>
  <div class="contact-line c-phone"><span class="ic"><svg width="11" height="11" viewBox="0 0 24 24"><path d="M6.6 10.8a15 15 0 0 0 6.6 6.6l2.2-2.2c.3-.3.7-.4 1-.2 1.1.4 2.3.6 3.6.6.6 0 1 .4 1 1V20c0 .6-.4 1-1 1A17 17 0 0 1 3 4c0-.6.4-1 1-1h3.5c.6 0 1 .4 1 1 0 1.3.2 2.5.6 3.6.1.3 0 .7-.2 1z" fill="#0a1822"/></svg></span>(800) 647-2915 x 42</div>
  <div class="contact-line c-web"><span class="ic"><svg width="12" height="12" viewBox="0 0 24 24" fill="none" stroke="#0a1822" stroke-width="2"><circle cx="12" cy="12" r="9"/><path d="M3 12h18M12 3c3 3 3 15 0 18M12 3c-3 3-3 15 0 18"/></svg></span>www.bluegatelendco.com</div>
  <div class="nmls">NMLS #381640</div>
</section>

<section class="card back">
  <div class="couple-photo" role="img" aria-label="Worried couple reviewing bills at a kitchen table"></div>
  <h2 class="solution-title">YOUR HOME EQUITY<br>COULD BE THE</h2>
  <div class="solution-script">Solution</div>
  <div class="rule"></div>

  <div class="notices">
    <p class="col-head">If you have received notices regarding:</p>
    <ul class="bullets">
      <li>Delinquent Property Taxes</li>
      <li>HOA or Condo Association Assessments</li>
      <li>Municipal Utility Liens</li>
      <li>Special Assessments</li>
      <li>Other Property-Related Obligations</li>
    </ul>
  </div>

  <div class="programs">
    <p class="col-head">You may qualify for financing options designed to help satisfy those obligations and bring your property current.</p>
    <p>Our experienced mortgage professionals can review your situation and discuss available programs, including:</p>
    <ul class="bullets">
      <li>Cash-Out Refinancing</li>
      <li>Home Equity Lines of Credit (HELOCs)</li>
      <li>Home Equity Loans</li>
      <li>Debt Consolidation Solutions</li>
    </ul>
  </div>

  <div class="offer-band">
    <div class="offer" style="left:37px"><span class="ring"><svg width="20" height="20" viewBox="0 0 24 24" fill="none" stroke="#fff" stroke-width="1.4"><circle cx="7" cy="8" r="2.5"/><circle cx="17" cy="8" r="2.5"/><path d="M3 19v-4a4 4 0 0 1 8 0v4M13 19v-4a4 4 0 0 1 8 0v4M10 13h4"/></svg></span>Free Consultation</div>
    <div class="offer" style="left:281px"><span class="ring"><svg width="20" height="20" viewBox="0 0 24 24" fill="none" stroke="#fff" stroke-width="1.4"><path d="M2 9l4-3 4 2 3-2 4 1 5 2M2 9l3 6 5 3 3-1 5-4 4-4M9 12l3 3"/></svg></span>No Obligation</div>
  </div>

  <div class="agent-card" role="img" aria-label="Portrait of the mortgage professional"></div>
  <div class="contact-script">Contact</div>
  <div class="agent-name">MARCUS DELANEY</div>
  <div class="agent-title">TRUSTED MORTGAGE PROFESSIONAL</div>
  <div class="contact-line c-phone"><span class="ic"><svg width="11" height="11" viewBox="0 0 24 24"><path d="M6.6 10.8a15 15 0 0 0 6.6 6.6l2.2-2.2c.3-.3.7-.4 1-.2 1.1.4 2.3.6 3.6.6.6 0 1 .4 1 1V20c0 .6-.4 1-1 1A17 17 0 0 1 3 4c0-.6.4-1 1-1h3.5c.6 0 1 .4 1 1 0 1.3.2 2.5.6 3.6.1.3 0 .7-.2 1z" fill="#111"/></svg></span>(800) 647-2915 x 42</div>
  <div class="contact-line c-web"><span class="ic"><svg width="12" height="12" viewBox="0 0 24 24" fill="none" stroke="#111" stroke-width="2"><circle cx="12" cy="12" r="9"/><path d="M3 12h18M12 3c3 3 3 15 0 18M12 3c-3 3-3 15 0 18"/></svg></span>www.bluegatelendco.com</div>
  <div class="nmls">NMLS #381640</div>

  <div class="foot-gold"></div>
  <div class="foot-blue"></div>
</section>

</body>
</html>
```